DL size flyer for home cleaning business

I need some graphic design.
i need a flyer designed for our home cleaning business, the img i have posted is a basic one we made but we want a proffesional one made.
that is our logo and all the test on that design is what we wish to have on the new flyer.

```html
<!DOCTYPE html>
<html lang="en">
<head>
<meta charset="utf-8">
<title>Brightway Cleaning – DL Flyer</title>
<link rel="stylesheet" href="https://fonts.googleapis.com/css2?family=Oswald:wght@500&family=Roboto:wght@500;700&display=swap">
<style>
  :root {
    --page-bg: #f6e3e4;
    --flyer-blue: #1f5593;
    --swoosh-green: #3c9a3a;
    --logo-blue: #2a66b0;
    --white: #ffffff;
    --photo-light: #e9ecea;
    --photo-mid: #b9c3bc;
    --photo-green: #52745e;
  }
  * { margin: 0; padding: 0; box-sizing: border-box; }
  html, body { width: 1200px; height: 900px; overflow: hidden; }
  body { background: var(--page-bg); font-family: "Roboto", sans-serif; color: var(--white); }

  .flyer { position: absolute; left: 397px; top: 67px; width: 404px; height: 767px; overflow: hidden; background: var(--flyer-blue); }
  .flyer-bg { position: absolute; inset: 0; }

  .logo-panel { position: absolute; left: 156px; top: 296px; width: 248px; height: 96px; background: var(--white);
    display: flex; align-items: center; gap: 10px; padding-left: 12px; }
  .logo-dot { width: 46px; height: 46px; border-radius: 50%; background: var(--logo-blue); flex: none; }
  .logo-name { font-family: "Roboto", sans-serif; font-weight: 700; font-size: 25px; line-height: 1; color: var(--logo-blue); }

  .tagline { position: absolute; left: 25px; top: 396px; width: 360px; font-family: "Oswald", sans-serif; font-weight: 500;
    font-size: 20px; line-height: 28px; text-transform: uppercase; letter-spacing: 0.2px; }

  .services { position: absolute; left: 27px; top: 456px; list-style: none; }
  .services li { display: flex; align-items: center; height: 28px; font-weight: 700; font-size: 19.5px; }
  .services svg { width: 30px; height: 22px; margin-right: 8px; flex: none; }

  .social { position: absolute; left: 63px; top: 605px; display: flex; align-items: center; gap: 10px; font-weight: 700; font-size: 19.5px; }
  .social-dot { width: 50px; height: 50px; border-radius: 50%; background: #4a73b8; border: 2px solid #8fa8d6; }

  .quote { position: absolute; left: 63px; top: 651px; font-weight: 700; font-size: 21px; letter-spacing: 0.3px; }

  .contacts { position: absolute; left: 105px; top: 680px; list-style: none; }
  .contacts li { display: flex; align-items: center; height: 28px; font-weight: 700; font-size: 13.5px; }
  .contacts svg { width: 16px; height: 14px; margin-right: 6px; }

  .email { position: absolute; left: 25px; top: 730px; display: flex; align-items: center; font-weight: 700; font-size: 13.5px; }
  .email svg { width: 12px; height: 9px; margin-right: 5px; }
</style>
</head>
<body>
  <article class="flyer">
    <svg class="flyer-bg" viewBox="0 0 404 767" aria-hidden="true">
      <defs>
        <linearGradient id="photoTone" x1="0" y1="0" x2="1" y2="1">
          <stop offset="0" stop-color="var(--photo-green)"/>
          <stop offset="0.35" stop-color="var(--photo-light)"/>
          <stop offset="0.75" stop-color="var(--photo-mid)"/>
          <stop offset="1" stop-color="#c9c07a"/>
        </linearGradient>
      </defs>
      <rect class="flyer-photo" width="404" height="420" fill="url(#photoTone)" role="img" aria-label="Photo of uniformed cleaners wiping a table and mopping in a bright living room"/>
      <path class="swoosh-green" d="M0,360 C90,300 240,232 404,222 L404,767 L0,767 Z" fill="var(--swoosh-green)"/>
      <path class="swoosh-blue" d="M0,408 C100,330 250,255 404,240 L404,767 L0,767 Z" fill="var(--flyer-blue)"/>
    </svg>

    <div class="logo-panel">
      <span class="logo-dot"></span>
      <span class="logo-name">Brightway Cleaning</span>
    </div>

    <h1 class="tagline">High quality, reliable, efficient,<br>dedicated cleaners</h1>

    <ul class="services">
      <li><svg viewBox="0 0 30 22"><rect x="1" y="5" width="18" height="16" fill="none" stroke="#fff" stroke-width="2"/><path d="M5 12 L10 17 L28 2" fill="none" stroke="#fff" stroke-width="3"/></svg>Regular cleans</li>
      <li><svg viewBox="0 0 30 22"><rect x="1" y="5" width="18" height="16" fill="none" stroke="#fff" stroke-width="2"/><path d="M5 12 L10 17 L28 2" fill="none" stroke="#fff" stroke-width="3"/></svg>One off cleans</li>
      <li><svg viewBox="0 0 30 22"><rect x="1" y="5" width="18" height="16" fill="none" stroke="#fff" stroke-width="2"/><path d="M5 12 L10 17 L28 2" fill="none" stroke="#fff" stroke-width="3"/></svg>End of lease cleans</li>
      <li><svg viewBox="0 0 30 22"><rect x="1" y="5" width="18" height="16" fill="none" stroke="#fff" stroke-width="2"/><path d="M5 12 L10 17 L28 2" fill="none" stroke="#fff" stroke-width="3"/></svg>Commercial / office cleans</li>
      <li><svg viewBox="0 0 30 22"><rect x="1" y="5" width="18" height="16" fill="none" stroke="#fff" stroke-width="2"/><path d="M5 12 L10 17 L28 2" fill="none" stroke="#fff" stroke-width="3"/></svg>Builders cleans</li>
    </ul>

    <p class="social">Like us on Linkup <span class="social-dot"></span></p>

    <p class="quote">CALL FOR A FREE QUOTE</p>

    <ul class="contacts">
      <li><svg viewBox="0 0 16 14"><path d="M1 4 Q8 -1 15 4 L13 6 L11 4 L5 4 L3 6 Z M4 6 L12 6 L14 13 L2 13 Z" fill="#fff"/></svg>Megan - 0400512637</li>
      <li><svg viewBox="0 0 16 14"><path d="M1 4 Q8 -1 15 4 L13 6 L11 4 L5 4 L3 6 Z M4 6 L12 6 L14 13 L2 13 Z" fill="#fff"/></svg>Dana - 0400781942</li>
    </ul>

    <p class="email"><svg viewBox="0 0 12 9"><rect x="0.5" y="0.5" width="11" height="8" fill="#fff"/><path d="M0.5 0.5 L6 5 L11.5 0.5" fill="none" stroke="#1f5593" stroke-width="1"/></svg>brightwaycleaninghillside@mailbox.com</p>
  </article>
</body>
</html>
```